Floral Design for Weddings And Events

I create floral designs for weddings and events. I create unusual designs that people will remember.

Industry/Entity Type

Floral

Contact Information for Business Card

Petals
Weddings and Events
Marlene Hayward, owner/designer
3718 Delwood Ct
San Marcos, CA 92078
marlenehaywardq@mailvista.net
530 555-0172

Requirements
Must have
• I would like the name of the business, PETALS, to Stand Out!! I like clean, bold lines.. nothing foo-foo! Must be easy to read I'm looking for a design that catches your eye and represents my creativity. I want my card to show the potential customer that I'm unique and creative
Nice to have
• I'm thinking of the name PETALS maybe worked into the design... I'm open to your creative ideas!!!! The name must be very legible
Should not have
• I'm open to any colors other that pink and yellow..nothing Foo-Foo or flowery..

```html
<!DOCTYPE html>
<html lang="en">
<head>
<meta charset="utf-8">
<title>Petals – Business Cards</title>
<link rel="stylesheet" href="https://fonts.googleapis.com/css2?family=Cinzel:wght@400;600&family=Arimo:wght@400&display=swap">
<style>
  :root {
    --backdrop: #d9d9dc;
    --berry: #861150;
    --berry-text: #a8195e;
    --ink: #070707;
    --ink-soft: #1b1b1b;
    --paper-white: #f1f3f1;
  }
  * { box-sizing: border-box; margin: 0; padding: 0; }
  html, body {
    width: 1200px; height: 960px; overflow: hidden;
    background: var(--backdrop);
  }
  .canvas {
    position: relative; width: 1200px; height: 960px;
    display: flex; justify-content: center; align-items: center; gap: 60px;
  }
  .card {
    position: relative; width: 380px; height: 665px;
    box-shadow: 0 12px 30px rgba(0,0,0,.25);
    font-family: "Arimo", Arial, sans-serif;
  }
  .card--berry { background: var(--berry); color: var(--ink-soft); }
  .card--ink { background: var(--ink); color: var(--berry-text); }

  .brand {
    position: absolute; top: 58px; right: 34px; text-align: right;
    color: var(--paper-white);
  }
  .brand__name {
    font-family: "Cinzel", Georgia, serif; font-weight: 400;
    font-size: 74px; line-height: 1; letter-spacing: 1px;
  }
  .brand__tagline {
    margin-top: 8px; font-size: 17px; letter-spacing: .5px;
  }

  .person {
    position: absolute; top: 262px; left: 48px;
  }
  .person__name {
    font-family: "Cinzel", Georgia, serif; font-weight: 400;
    font-size: 30px; letter-spacing: 1px; white-space: nowrap;
  }
  .person__role {
    margin-top: 2px; margin-left: 40px;
    font-size: 17px; color: var(--paper-white);
  }

  .contact {
    position: absolute; top: 410px; left: 0; right: 0;
    text-align: center; font-size: 19px; line-height: 1.6;
    font-style: normal;
  }
  .contact__phone { margin-bottom: 6px; }
</style>
</head>
<body>
<main class="canvas">
  <article class="card card--berry">
    <header class="brand">
      <div class="brand__name">Petals</div>
      <div class="brand__tagline">Weddings and Events</div>
    </header>
    <div class="person">
      <h1 class="person__name">MARLENE HAYWARD</h1>
      <p class="person__role">owner/designer</p>
    </div>
    <address class="contact">
      <div class="contact__phone">530 555-0172</div>
      <div>marlenehaywardq@mailvista.net</div>
      <div>3718 Delwood Ct San Marcos,</div>
      <div>CA 92078</div>
    </address>
  </article>

  <article class="card card--ink">
    <header class="brand">
      <div class="brand__name">Petals</div>
      <div class="brand__tagline">Weddings and Events</div>
    </header>
    <div class="person">
      <h2 class="person__name">MARLENE HAYWARD</h2>
      <p class="person__role">owner/designer</p>
    </div>
    <address class="contact">
      <div class="contact__phone">530 555-0172</div>
      <div>marlenehaywardq@mailvista.net</div>
      <div>3718 Delwood Ct San Marcos,</div>
      <div>CA 92078</div>
    </address>
  </article>
</main>
</body>
</html>
```